Banner Ad for Resume Services Website

The add is for this web site: www.BrightCareerPages.net

The site offers 4 different services:

- Resume Writing (by a Certified Professional Resume Writer)
- Resume Posting (posts your resume to 85 job sites)
- Resume Distribution (sends your resume to hundreds of recruiters)
- Resume Online website (created an online resume with a domain name to your name)

Colors to be used are Blue, Yellow, etc... please check the website for inspiration.

Check the web site to learn more.

Target Market(s)

Unemployed, Professionals who want to switch jobs, etc..

Industry/Entity Type

Requirements
Must have
• We definitely one this to be included on the banner:

"Free Resume Samples"

in order to attract clicks.
Nice to have
• Some of the words we suggest to include on the banner are:

"How Good is Your Resume? Ask a Professional !"

Should not have
• No animation !

Do not place the LOGO on the banner as our LOGO might change in the near future. If you already submitted a banner with the LOGO on it, you can replace it with any other graphic that has a Resume/Jobs/BusinessStaff related theme.

```html
<!DOCTYPE html>
<html lang="en">
<head>
<meta charset="utf-8">
<title>Resume Services Banner</title>
<link href="https://fonts.googleapis.com/css2?family=Roboto+Condensed:wght@700;800&display=swap" rel="stylesheet">
<style>
  :root {
    --navy-deep: #0a1660;
    --navy: #14268f;
    --blue-mid: #2a49c8;
    --blue-light: #4c72e6;
    --headline-yellow: #f7f200;
    --badge-green: #c7de6c;
    --badge-green-edge: #a9c648;
    --badge-text: #1c2600;
    --photo-dark: #4a5a6e;
    --photo-light: #c9d3dc;
  }
  html, body {
    margin: 0;
    padding: 0;
    width: 1200px;
    height: 148px;
    overflow: hidden;
    background: #ffffff;
  }
  .banner {
    position: relative;
    width: 1200px;
    height: 148px;
    overflow: hidden;
    background:
      radial-gradient(ellipse 420px 160px at 700px 90px, var(--blue-light) 0%, var(--blue-mid) 45%, transparent 80%),
      linear-gradient(90deg, var(--navy-deep) 0%, var(--navy) 40%, var(--navy) 70%, var(--navy-deep) 100%);
    font-family: "Roboto Condensed", "Arial Narrow", sans-serif;
  }
  .banner__photo {
    position: absolute;
    left: 0;
    top: 0;
    width: 380px;
    height: 148px;
    background: linear-gradient(90deg, var(--photo-dark) 0%, var(--photo-light) 45%, #8d9bb0 75%, var(--navy) 100%);
  }
  .banner__headline {
    position: absolute;
    left: 380px;
    width: 660px;
    top: 14px;
    margin: 0;
    text-align: center;
    color: var(--headline-yellow);
    font-weight: 800;
    font-size: 45px;
    line-height: 54px;
    letter-spacing: 0.3px;
    text-shadow: 2px 2px 0 #050b3a;
  }
  .banner__headline span { display: block; }
  .banner__badge {
    position: absolute;
    left: 1058px;
    top: 4px;
    width: 142px;
    height: 144px;
    box-sizing: border-box;
    background: var(--badge-green);
    border: 2px solid var(--badge-green-edge);
    border-radius: 10px 0 0 10px;
    display: flex;
    flex-direction: column;
    justify-content: center;
    align-items: center;
    color: var(--badge-text);
    font-weight: 700;
    font-size: 27px;
    line-height: 33px;
    text-align: center;
  }
</style>
</head>
<body>
  <div class="banner">
    <div class="banner__photo" role="img" aria-label="Photo of two business professionals shaking hands in an office"></div>
    <h1 class="banner__headline">
      <span>How Good is Your Resume?</span>
      <span>Ask a Professional !</span>
    </h1>
    <div class="banner__badge">
      <span>Free</span>
      <span>Resume</span>
      <span>Samples</span>
    </div>
  </div>
</body>
</html>
```